Vitalune - Label design for a supplement with probiotic and prebiotic

Hello, we are a supplement company and we need a label design for our first product. The product's name is Vitalune and the company's name is Koravex Nutrition (Logo attached, It is allowed to change the color) and we are located in Orlando, if we like the label, in the future we can make other products too.
Our product is a supplement that contains probiotics, prebiotics and other vitamins, it will be packaged in a 300g plastic jar (Img attached), we like simple but premium-looking packaging.
Below are some links to brands and products we like:
https://www.shopvarelt.example/stores/page/7D1188AA-5521-4E9B-B302-B1A447FE22CC?ingress=2&visitId=91b2ccd4-774e-408a-bb21-c4e8f1aa2093&ref_=bl_dp_s_web_58213044022
https://www.shopvarelt.example/stores/page/61AB4E3D-92C1-4A77-9D20-7EE350173B81?ingress=2&visitId=8812fa0e-311c-4d2a-a7f4-1b9c30e44f12&ref_=bl_dp_s_web_24417720933
https://www.shopvarelt.example/stores/Teluvo+Nutrition/page/C2288340-5E61-4B19-93A4-12307C88D29E?store_ref=SLP_FW_450D77AB-C12E-4A98-A31F-2207E5C9A611
https://www.shopvarelt.example/stores/page/AA2C46DE-71F9-4B22-C390-5EEDC81B309F?ingress=2&visitId=15e93b27-6a0c-4f3e-9bd1-a7c2301ee9b4&ref_=bl_dp_s_web_4182930055
https://www.shopvarelt.example/stores/node/39527164022?_encoding=UTF8&field-lbr_brands_browse-bin=QUILMAXNUTRITION&ref_=bl_dp_s_web_39527164022
https://www.shopvarelt.example/stores/page/2B3E8804-6611-4C2A-9F17-E8A913B02C57?ingress=6&visitId=4461d09c-b12a-4d7e-8fa1-09c5d3e6bb21&store_ref=storeRecs_Instant_27316488033
Updates
Hi, This product will be packaged in a 300g bottle, it is allowed to insert images and it is very important to inform "100 Billion live bacteria", 5 grams of probiotic, 5 grams of prebiotic and orange flavor.
The bottle is rounded, the size of the art must be 2.87 in and 10.74 in, I will need barcode space, supplement facts, directions and warning. This information I can put later.
Target Market(s)
Our target is people who wish to have a healthier recovery after undergoing cancer treatments, helping to maintain health, improving quality of life and reducing the harm that these treatments cause.
Requirements
Must have
- It is very important that the product contains the following information:
- 100 Billion live bacteria
- 5 grams of probiotic and 5 grams of prebiotic
- No artificial flavours
- Space for barcode
Amount per container: 10.6 oz (300 g)
Serving size: 1 scoop (10 grams)
Servings per container: 30
Amount per serving
Calories 15 Calories from fat 0
Total Fat 0
Total Carbohydrate 5g
Dietary fiber 4g
Sugars 1g
Protein 0g
Proprietary Probiotic blend: 5 billons
Lactobacillus acidophilus
Bifidobacterium animalis subsp. lactis.
Other ingredients: Organic inulin fiber, stevia, natural orange flavor, citric acid, riboflavin Not a significant source of cholesterol, fat and protein
Nice to have
- We like simple design
Should not have
- Images from brolen photos.

```html
<!DOCTYPE html>
<html lang="en">
<head>
<meta charset="utf-8">
<title>Koravex Nutrition – Probiotic &amp; Prebiotic Label</title>
<link rel="stylesheet" href="https://fonts.googleapis.com/css2?family=Noto+Serif:wght@400;700&family=Arimo:wght@400;700&family=Barlow:wght@400&display=swap">
<style>
  :root{
    --green:#2db67c;
    --grey:#8e8e8e;
    --grey-light:#c9c9c9;
    --ink:#1f1f1f;
    --paper:#ffffff;
    --backdrop:#f4f4f4;
    --serif:"Noto Serif", Georgia, serif;
    --sans:"Arimo", Arial, sans-serif;
    --label:"Barlow", Arial, sans-serif;
  }
  *{box-sizing:border-box;margin:0;padding:0}
  html,body{width:1200px;height:653px;overflow:hidden;background:var(--backdrop)}
  .canvas{position:relative;width:1200px;height:653px}
  .label{position:absolute;left:40px;top:176px;width:1120px;height:300px;background:var(--paper);overflow:hidden;box-shadow:0 2px 10px rgba(0,0,0,.08)}
  .band-top{position:absolute;left:0;top:0;width:100%;height:14px;background:var(--green)}
  .band-bottom{position:absolute;left:0;bottom:10px;width:100%;height:5px;background:var(--green)}
  .panel{position:absolute;top:0;height:100%}
  .panel--back{left:0;width:330px}
  .panel--front{left:330px;width:460px}
  .panel--facts{left:790px;width:330px}

  /* back panel */
  .copy{position:absolute;left:16px;font-family:var(--serif);font-size:8.4px;line-height:1.3;color:var(--ink);width:300px}
  .copy h3{font-size:9.5px;font-weight:400;color:var(--green);margin-bottom:3px}
  .copy--directions{top:46px}
  .copy--use{top:136px}
  .warning{position:absolute;left:16px;top:182px;width:300px;border:1.5px solid var(--ink);padding:4px 6px;font-family:var(--serif);font-size:8.4px;line-height:1.3;color:var(--ink)}
  .warning strong{display:block;font-weight:400;font-size:9.5px}
  .badges{position:absolute;left:18px;top:232px;display:flex;gap:18px}
  .badge{display:flex;flex-direction:column;align-items:center;font-family:var(--label);font-size:10px;color:var(--green)}
  .badge-mark{width:30px;height:30px;border-radius:50%;border:2.5px solid var(--green);margin-bottom:4px}
  .badge-mark--solid{background:var(--green)}

  /* front panel */
  .tab-front{position:absolute;left:0;top:14px;width:110px;height:32px;background:var(--green);border-bottom-right-radius:26px}
  .brand{position:absolute;left:128px;top:22px;font-family:var(--serif);font-weight:700;font-size:16px;color:var(--green);letter-spacing:.2px;white-space:nowrap}
  .headline{position:absolute;left:40px;top:68px;font-family:var(--serif);font-weight:700;font-size:33px;line-height:1.12;color:var(--green);white-space:nowrap}
  .ampersand{position:absolute;left:238px;top:54px;font-family:var(--serif);font-weight:700;font-size:78px;color:var(--grey);line-height:1}
  .tagline{position:absolute;left:40px;top:150px;font-family:var(--serif);font-weight:700;font-size:21px;color:var(--ink);white-space:nowrap}
  .claims{position:absolute;left:40px;top:190px;display:flex;align-items:center;font-family:var(--serif);font-weight:700;color:var(--green);white-space:nowrap}
  .claim{display:flex;align-items:center;gap:5px;padding-right:7px}
  .claim + .claim{border-left:2px solid var(--green);padding-left:7px}
  .claim-figure{font-size:25px;line-height:1}
  .claim-text{font-size:11px;line-height:1.05}
  .supplement{position:absolute;left:40px;top:236px;font-family:var(--serif);font-weight:700;font-size:13px;color:var(--ink);padding:0 12px 3px 0;border-bottom:3px solid var(--grey)}
  .net-weight{position:absolute;right:50px;bottom:15px;height:26px;padding:0 12px 0 38px;background:var(--green);color:var(--paper);font-family:var(--serif);font-weight:700;font-size:10.5px;display:flex;align-items:center;border-top-left-radius:20px;white-space:nowrap}
  .molecule{position:absolute;left:340px;top:70px;width:100px;height:160px;border-radius:50%;background:radial-gradient(circle,#dcdcdc 0%,#eeeeee 60%,#ffffff 100%)}

  /* facts panel */
  .facts{position:absolute;left:92px;top:22px;width:222px;border:1.5px solid var(--ink);padding:3px 5px;font-family:var(--sans);font-size:8px;color:var(--ink);line-height:1.22}
  .facts-title{font-weight:700;font-size:20px;line-height:1}
  .facts-row{display:flex;justify-content:space-between;border-top:1px solid var(--ink)}
  .facts-row--thick{border-top:5px solid var(--ink)}
  .facts-row--mid{border-top:3px solid var(--ink)}
  .facts-row .indent{padding-left:10px}
  .facts-small{font-size:6.5px;text-align:right;border-top:1px solid var(--ink)}
  .facts-foot{display:flex;justify-content:space-between}
  .manufacturer{position:absolute;left:92px;top:246px;font-family:var(--serif);color:var(--grey);font-size:8.5px;line-height:1.2}
  .manufacturer strong{font-size:11px;display:block}
  .barcode-space{position:absolute;left:236px;top:244px;width:78px;height:38px;background:var(--grey-light)}
</style>
</head>
<body>
<div class="canvas">
  <div class="label">
    <div class="band-top"></div>
    <div class="band-bottom"></div>

    <section class="panel panel--back">
      <div class="copy copy--directions">
        <h3>Directions</h3>
        <p>Lorem ipsum dolor sit amet, consectetuer adipiscing elit, sed diam nonummy nibh euismod tincidunt ut laoreet dolore magna aliquam erat volutpat. Ut wisi enim ad minim veniam, quis nostrud exerci tation ullamcorper suscipit lobortis nisl ut aliquip ex ea commodo consequat. Duis autem vel eum iriure dolor in hendrerit in vulputate velit esse molestie consequat.</p>
      </div>
      <div class="copy copy--use">
        <h3>How to Use</h3>
        <p>Lorem ipsum dolor sit amet, consectetuer adipiscing elit, sed diam nonummy nibh euismod tincidunt ut laoreet dolore magna aliquam erat</p>
      </div>
      <div class="warning">
        <strong>WARNING</strong>
        Lorem ipsum dolor sit amet, consectetuer adipiscing elit, sed diam nonummy nibh euismod tincidunt ut laoreet dolore erat.
      </div>
      <div class="badges">
        <div class="badge"><span class="badge-mark"></span>Gluten Free</div>
        <div class="badge"><span class="badge-mark"></span>Lactose Free</div>
        <div class="badge"><span class="badge-mark"></span>Kosher Certified</div>
        <div class="badge"><span class="badge-mark badge-mark--solid"></span>Non GMO</div>
      </div>
    </section>

    <section class="panel panel--front">
      <div class="tab-front"></div>
      <div class="brand">KORAVEX NUTRITION</div>
      <h1 class="headline">PROBIOTIC<br>PREBIOTIC</h1>
      <div class="ampersand">&amp;</div>
      <div class="tagline">100 Billion live bacteria</div>
      <div class="claims">
        <div class="claim"><span class="claim-figure">5</span><span class="claim-text">grams of<br>probiotic</span></div>
        <div class="claim"><span class="claim-figure">5</span><span class="claim-text">grams of<br>prebiotic</span></div>
        <div class="claim"><span class="claim-figure">No</span><span class="claim-text">artificial<br>flavours</span></div>
      </div>
      <div class="supplement">DIETARY SUPPLEMENT</div>
      <div class="molecule" role="img" aria-label="Grey line illustration of connected molecule nodes and bacteria rings"></div>
      <div class="net-weight">NET WT. 485G (1.07 LBS)</div>
    </section>

    <section class="panel panel--facts">
      <div class="facts">
        <div class="facts-title">Nutrition Facts</div>
        <div>Serving Size 95 g</div>
        <div class="facts-row facts-row--thick"><strong>Amount Per Serving</strong></div>
        <div class="facts-row"><span><strong>Calories</strong> 231</span><span>Calories from Fat 154</span></div>
        <div class="facts-small">% Daily Value*</div>
        <div class="facts-row"><span><strong>Total Fat</strong> 17.2g</span><strong>26%</strong></div>
        <div class="facts-row"><span class="indent">Saturated Fat 5.8g</span><strong>29%</strong></div>
        <div class="facts-row"><span class="indent"><em>Trans</em> Fat 0.0g</span><span></span></div>
        <div class="facts-row"><span><strong>Cholesterol</strong> 0mg</span><strong>0%</strong></div>
        <div class="facts-row"><span><strong>Sodium</strong> 87mg</span><strong>4%</strong></div>
        <div class="facts-row"><span><strong>Potassium</strong> 293mg</span><strong>8%</strong></div>
        <div class="facts-row"><span><strong>Total Carbohydrates</strong> 18.6g</span><strong>6%</strong></div>
        <div class="facts-row"><span class="indent">Dietary Fiber 5.3g</span><strong>21%</strong></div>
        <div class="facts-row"><span class="indent">Sugars 11.0g</span><span></span></div>
        <div class="facts-row facts-row--mid"><span><strong>Protein</strong> 2.5g</span><span></span></div>
        <div class="facts-row facts-row--thick"><span>Vitamin A 2%</span><span>Vitamin C 10%</span></div>
        <div class="facts-foot"><span>Calcium 4%</span><span>Iron 2%</span></div>
      </div>
      <div class="manufacturer">
        <strong>Manufacture:</strong>
        Koravex Nutrition<br>Ph: 0100 555 0142
      </div>
      <div class="barcode-space"></div>
    </section>
  </div>
</div>
</body>
</html>
```